Business Card Design

Please use the Logo for colors and styles, and create a business card using the following info:

Matthias Loeber
Web Developer

Loeber Solutions
+41 76 482 17 05
matthias@loeber-solutions.example
www.loeber-solutions.example

Download the logo at http://loeber-solutions.example/tl_files/loeber_solutions.zip

Thanks for your works!

```html
<!DOCTYPE html>
<html lang="en">
<head>
<meta charset="utf-8">
<title>Loeber Solutions – Business Card</title>
<link rel="stylesheet" href="https://fonts.googleapis.com/css2?family=Jost:wght@400;500&display=swap">
<style>
  :root {
    --navy: #2b4f80;
    --navy-deep: #234470;
    --sky: #2f7fc4;
    --paper: #ffffff;
    --ink-light: #e8eef6;
    --stage: #dfe3e8;
  }
  * { box-sizing: border-box; margin: 0; padding: 0; }
  html, body {
    width: 1200px; height: 960px; overflow: hidden;
    background: var(--stage);
    font-family: "Jost", "Futura", sans-serif;
  }
  .canvas {
    width: 1200px; height: 960px;
    display: flex; flex-direction: column; align-items: center; justify-content: center;
    gap: 48px;
  }
  .card {
    width: 700px; height: 400px;
    box-shadow: 0 10px 30px rgba(30, 50, 80, 0.18);
    position: relative; overflow: hidden;
  }
  .wordmark {
    font-weight: 500; letter-spacing: 0.02em; text-transform: uppercase;
    white-space: nowrap;
  }

  /* Front */
  .card-front {
    background: var(--navy);
    display: flex; align-items: center; justify-content: center;
  }
  .card-front .wordmark { color: var(--paper); font-size: 50px; }

  /* Back */
  .card-back { background: var(--paper); }
  .card-back .brand-band {
    height: 172px; display: flex; align-items: center; justify-content: center;
  }
  .card-back .wordmark { color: var(--sky); font-size: 34px; }
  .card-back .rule { height: 3px; background: var(--sky); }
  .card-back .info-band {
    position: absolute; left: 0; right: 0; top: 175px; bottom: 0;
    background: var(--navy);
    display: flex; align-items: center;
    color: var(--ink-light);
  }
  .identity { width: 50%; padding-left: 40px; }
  .identity .person { font-size: 27px; line-height: 1.15; }
  .identity .role { font-size: 27px; line-height: 1.15; }
  .identity .company { font-size: 19px; margin-top: 12px; }
  .divider { width: 1px; height: 130px; background: rgba(255,255,255,0.45); }
  .contacts { list-style: none; padding-left: 44px; font-size: 19px; line-height: 1.5; }
  .contacts li { display: flex; align-items: center; gap: 10px; }
  .contacts svg { width: 13px; height: 13px; fill: var(--ink-light); flex: none; }
</style>
</head>
<body>
<main class="canvas">
  <section class="card card-front" aria-label="Card front">
    <span class="wordmark">Loeber Solutions</span>
  </section>

  <section class="card card-back" aria-label="Card back">
    <div class="brand-band"><span class="wordmark">Loeber Solutions</span></div>
    <div class="rule"></div>
    <div class="info-band">
      <div class="identity">
        <p class="person">Matthias Loeber</p>
        <p class="role">Web Developer</p>
        <p class="company">Loeber Solutions</p>
      </div>
      <div class="divider"></div>
      <ul class="contacts">
        <li>
          <svg viewBox="0 0 16 16" aria-hidden="true"><path d="M4 1l3 3-2 2c1 2 3 4 5 5l2-2 3 3-2 3C7 15 1 9 1 3z"/></svg>
          +41 76 482 17 05
        </li>
        <li>
          <svg viewBox="0 0 16 16" aria-hidden="true"><path d="M1 3h14v10H1z M1 3l7 6 7-6" stroke="#2b4f80" stroke-width="1.4"/></svg>
          matthias@loeber-solutions.example
        </li>
        <li>
          <svg viewBox="0 0 16 16" aria-hidden="true"><circle cx="8" cy="8" r="7"/><path d="M1 8h14M8 1c-3 4-3 10 0 14M8 1c3 4 3 10 0 14" stroke="#2b4f80" stroke-width="1" fill="none"/></svg>
          www.loeber-solutions.example
        </li>
      </ul>
    </div>
  </section>
</main>
</body>
</html>
```